PL Dunmore Electric Yard Sign

Looking to have a yard sign designed that we can place at projects we are working on. Most likely will be 18" H x 24" W but flexible that we can increase the size if necessary. It should include our logo, our phone # 555-214-7796, website pldunmoreelectric.example and slogan, Wired with care, powered by pride. Colors should match our brand.

```html
<!DOCTYPE html>
<html lang="en">
<head>
<meta charset="utf-8">
<title>PL Dunmore Electric – Yard Sign</title>
<link href="https://fonts.googleapis.com/css2?family=Montserrat:wght@500;600;700&display=swap" rel="stylesheet">
<style>
  :root {
    --navy: #1c3764;
    --red: #e32b2f;
    --white: #ffffff;
    --backdrop: #ececec;
  }
  * { margin: 0; padding: 0; box-sizing: border-box; }
  html, body {
    width: 1200px;
    height: 846px;
    overflow: hidden;
    background: var(--backdrop);
  }
  .yard-sign {
    position: absolute;
    left: 60px;
    top: 18px;
    width: 1080px;
    height: 810px;
    background: var(--white);
    font-family: "Montserrat", Arial, sans-serif;
    color: var(--navy);
  }
  .brand {
    position: absolute;
    top: 200px;
    left: 0;
    width: 100%;
    height: 100px;
    display: flex;
    align-items: center;
    justify-content: center;
    gap: 26px;
  }
  .brand-mark {
    width: 46px;
    height: 46px;
    background: var(--red);
  }
  .brand-name {
    font-weight: 700;
    font-size: 72px;
    letter-spacing: 1px;
    line-height: 1;
    color: var(--navy);
  }
  .phone-band {
    position: absolute;
    top: 419px;
    left: 0;
    width: 100%;
    height: 120px;
    background: var(--navy);
    display: flex;
    align-items: center;
    justify-content: center;
  }
  .phone-number {
    color: var(--white);
    font-weight: 600;
    font-size: 112px;
    letter-spacing: 0;
    line-height: 1;
  }
  .website {
    position: absolute;
    top: 574px;
    width: 100%;
    text-align: center;
    font-size: 54px;
    font-weight: 500;
    line-height: 1.2;
  }
  .slogan {
    position: absolute;
    top: 700px;
    width: 100%;
    text-align: center;
    font-size: 47px;
    font-weight: 500;
    line-height: 1.2;
  }
</style>
</head>
<body>
  <main class="yard-sign">
    <div class="brand">
      <span class="brand-mark" aria-hidden="true"></span>
      <span class="brand-name">PL Dunmore Electric</span>
    </div>
    <div class="phone-band">
      <span class="phone-number">555-214-7796</span>
    </div>
    <p class="website">pldunmoreelectric.example</p>
    <p class="slogan">Wired with care, powered by pride</p>
  </main>
</body>
</html>
```